PuraVeln

Hi, We are looking for a design Label for our Packaged Drinking Water. We want a label in rich color. The current Label is uploaded. We wish for a much brighter color rather than black. Our current label is in black. We have attached other company labels to give you idea. The Solmira bottle image is also uploaded they use sticker for their bottle, front sticker contains name and back sticker's inner portion has graphics and the outer side has information we also open to that.
Industry/Entity Type
Packaged Drinking Water Bottle Brand
Look and feel
Each slider illustrates characteristics of the customer's brand and the style your logo design should communicate.

```html
<!DOCTYPE html>
<html lang="en">
<head>
<meta charset="UTF-8">
<title>PuraVeln Packaged Drinking Water Label</title>
<link href="https://fonts.googleapis.com/css2?family=Poppins:wght@400;500;600;700&family=Roboto+Condensed:wght@500&display=swap" rel="stylesheet">
<style>
  :root {
    --page-bg: #ececec;
    --label-light: #e8fafc;
    --label-mid: #b3e9f1;
    --label-deep: #7dd6e4;
    --brand-teal: #1c8e98;
    --ink: #203c46;
    --rule: #3a5660;
    --veg-green: #1a9a3c;
    --mountain-tone: 74, 170, 188;
  }
  * { box-sizing: border-box; margin: 0; padding: 0; }
  html, body {
    width: 1200px; height: 800px; overflow: hidden;
    background: var(--page-bg);
    font-family: "Poppins", sans-serif;
    color: var(--ink);
  }
  .label {
    position: absolute; left: 40px; top: 232px;
    width: 1120px; height: 336px;
    background:
      radial-gradient(ellipse at 30% 25%, rgba(255,255,255,0.75), transparent 55%),
      radial-gradient(ellipse at 75% 75%, rgba(125,214,228,0.5), transparent 60%),
      linear-gradient(160deg, var(--label-light) 0%, var(--label-mid) 55%, var(--label-deep) 100%);
    overflow: hidden;
  }
  .label > * { position: absolute; }

  .company-info { left: 23px; top: 31px; font-size: 11px; line-height: 13.6px; white-space: nowrap; }
  .company-info p + p { margin-top: 3px; }
  .cert-badge {
    left: 62px; top: 150px; width: 41px; height: 14px;
    border-radius: 3px; background: var(--brand-teal); opacity: 0.75;
  }
  .license-no {
    left: 27px; top: 168px; font-family: "Roboto Condensed", sans-serif;
    font-size: 12px; font-weight: 500; letter-spacing: -0.4px; white-space: nowrap;
  }
  .net-qty { left: 30px; top: 193px; font-size: 12px; font-weight: 700; }
  .standard-code {
    left: 169px; top: 147px; font-family: "Roboto Condensed", sans-serif;
    font-size: 9px; font-weight: 500;
  }
  .standard-badge {
    left: 159px; top: 159px; width: 57px; height: 48px;
    border: 3px solid var(--ink); border-radius: 8px;
  }
  .standard-licence {
    left: 151px; top: 210px; font-family: "Roboto Condensed", sans-serif;
    font-size: 8px; font-weight: 500; white-space: nowrap;
  }
  .care-icons { left: 25px; top: 227px; display: flex; gap: 12px; }
  .care-icons span { width: 19px; height: 19px; border: 2.5px solid var(--ink); }
  .care-icons span:nth-child(2n) { border-radius: 50%; }
  .usage-note { left: 29px; top: 278px; font-size: 11px; line-height: 14px; white-space: nowrap; }

  .veg-mark {
    left: 772px; top: 55px; width: 21px; height: 21px;
    border: 2px solid var(--veg-green); background: #fff;
    display: flex; align-items: center; justify-content: center;
  }
  .veg-mark::after { content: ""; width: 10px; height: 10px; border-radius: 50%; background: var(--veg-green); }
  .brand-name {
    left: 358px; top: 108px; font-size: 86px; font-weight: 600;
    color: var(--brand-teal); letter-spacing: 0.5px; line-height: 1;
  }
  .brand-tm { left: 758px; top: 110px; font-size: 12px; font-weight: 600; color: var(--brand-teal); }
  .brand-tagline {
    left: 360px; width: 400px; top: 207px; text-align: center;
    font-size: 14px; letter-spacing: 0.28em; color: var(--brand-teal);
  }
  .mountain-art {
    top: 230px; height: 106px;
    background: radial-gradient(ellipse at 50% 100%, rgba(var(--mountain-tone), 0.45) 0%, rgba(var(--mountain-tone), 0.2) 55%, rgba(var(--mountain-tone), 0) 75%);
  }
  .mountain-art.left { left: 284px; width: 270px; }
  .mountain-art.right { left: 566px; width: 270px; }

  .product-story, .nutrition-title {
    left: 866px; font-size: 9.6px; line-height: 13.2px;
    letter-spacing: -0.1px; white-space: nowrap;
  }
  .product-story { top: 33px; }
  .nutrition-title { top: 113px; }
  .nutrition-table {
    left: 867px; top: 144px; width: 228px;
    border-collapse: collapse; font-size: 9.5px; white-space: nowrap;
  }
  .nutrition-table td { border: 1px solid var(--rule); padding: 0 5px; height: 19.5px; }
  .contact { left: 866px; top: 225px; white-space: nowrap; }
  .contact .email { font-size: 10px; font-weight: 600; line-height: 14px; }
  .contact .care-line { font-size: 12px; font-weight: 700; line-height: 15px; }
  .fine-print { left: 868px; top: 258px; font-size: 8px; line-height: 12.4px; white-space: nowrap; }
</style>
</head>
<body>
  <section class="label">
    <div class="company-info">
      <p>Manufactured By:<br>Tarlin Jalseva Pvt Ltd<br>Meerpur Khurd, Nadigaon, Ranipur<br>Uttar Pradesh- 240117</p>
      <p>Marketed By:<br>BrightLeaf<br>Second Floor, Lakeview Colony, Neelghat<br>Ranipur, Uttar Pradesh- 240117</p>
    </div>
    <div class="cert-badge"></div>
    <div class="license-no">Lic. No. : 10493817265540</div>
    <div class="net-qty">Net Qty 1 L</div>
    <div class="standard-code">IS 14543</div>
    <div class="standard-badge"></div>
    <div class="standard-licence">CM/L-4815209377</div>
    <div class="care-icons"><span></span><span></span><span></span><span></span><span></span><span></span></div>
    <div class="usage-note">CRUSH THE BOTTLE AFTER USE<br>Best Before 6 Months from Packaging</div>

    <div class="veg-mark"></div>
    <div class="brand-name">PuraVeln</div>
    <div class="brand-tm">TM</div>
    <div class="brand-tagline">PACKAGED DRINKING WATER</div>
    <div class="mountain-art left" role="img" aria-label="Line-drawn mountain range illustration"></div>
    <div class="mountain-art right" role="img" aria-label="Line-drawn mountain range illustration"></div>

    <p class="product-story">Every Drop Of PuraVeln Water Goes Through<br>A Multistage Purification Process That<br>Includes Micron Filtration, Purification, UV,<br>Ozonation And With Add Minerals (Calcium<br>Chloride, Magnesium Sulphate &amp; Potassium<br>Bicarbonate).</p>
    <p class="nutrition-title">Nutritional Information<br>(Typical values per 100ml):</p>
    <table class="nutrition-table">
      <tr><td>Energy: 0 Kcal</td><td>Protein: 0 g</td></tr>
      <tr><td>Carbohydrate: 0 g</td><td>Calcium: 1.0 mg</td></tr>
      <tr><td>Sugar: 0 g</td><td>Magnesium: 0.5mg</td></tr>
      <tr><td>Fat: 0 g</td><td>Potassium: 0.1 mg</td></tr>
    </table>
    <div class="contact">
      <p class="email">hello@tarlinjalseva.com</p>
      <p class="care-line">Customer Care: +91-7400612958</p>
    </div>
    <p class="fine-print">For BIS Certification details, visit:www.qcdesk.in<br>For Manufacturing, "Date of Packaging",<br>Batch No. #MRP(Incl. of all taxes),<br>USP &amp; Expiry: Check Bottle Neck/Cap</p>
  </section>
</body>
</html>
```